To design a new professional and elegant website design

To design an elegant and professional business website - e.g. Responsive WordPress theme.

Please refer to the existing site www.verlow-partners.com for information regarding the business service and the content that will be included.

While the designer can suggest colors, the current logo (see attached) should remain.
Although I have indicated Sans Serif as a font, I welcome alternative suggestions.
Updates

To all designers:

I have attached additional .psd files of the logo for your use in the design of the new site (theme). As posted in an earlier response, I wish to keep the logo and the color blue. You are welcome to either work with or change the green.

- Please avoid making the page too busy.

- Avoid stock business pictures such as the people working on a document with the calculator the generic people in suits. Ideally, I would like unique media.

- Do not include contact information on the home page. There are two offices – 1 in Houston and one in UK and I want to make sure that we distinguish between the two.

- Use bullets rather than check boxes .

- Do not use the social links as we do not currently use them - this may change in the future

- The footer should include: sitemap, Terms of Use, Privacy Policy and the 2014 Copyright notice. The other pages should be accessible via a menu

Hope this helps.
Thanks

To all participants,

I have increased the budget by an additional £200.

Regards,

Target Market(s)

As you may glean from the website, the company is a management consultancy serving Meridale 400 companies and private equity firms. Companies include: Tolk, GX, KF, Navine Rosset Companies, Selo Varna...

Sites that may influence the design include:

http://www.hvn.co.uk/consulting/
http://www.qz.com/UK/en/Services/Advisory
http://www.kolt.com/industry-expertise/technology/index.aspx
http://www.obvaleprojects.com/news

Industry/Entity Type

Business Service

Font styles to use
Sans Serif

Colors

Designer to choose colors to be used in the design.

Requirements
Must have
• Existing blue logo - globe with the V & P (see attached). The green is not necessary
Must function of a WordPress responsive platform.
Nice to have
• While the new theme will need to be consistent throughout the site, the home page can vary from the child pages.
Should not have
• Common stock images. If used, the images and icons should be unique.

```html
<!DOCTYPE html>
<html lang="en">
<head>
<meta charset="utf-8">
<title>Verlow Partners — Home</title>
<link href="https://fonts.googleapis.com/css2?family=Montserrat:wght@400;600;700&family=Open+Sans:wght@400;600;700&family=Noto+Serif:wght@400&display=swap" rel="stylesheet">
<style>
  :root{
    --brand-blue:#1479c4;
    --quote-blue:#0a7cc6;
    --brand-green:#0f9a48;
    --accent-green:#3cc24a;
    --ink:#2f2f2f;
    --ink-soft:#555;
    --panel:rgba(236,238,240,0.93);
    --bar:rgba(30,32,36,0.82);
    --footer:#3b3b3b;
    --white:#fff;
  }
  *{margin:0;padding:0;box-sizing:border-box}
  html,body{width:1200px;height:601px;overflow:hidden;background:#fff}
  body{position:relative;font-family:"Open Sans",Arial,sans-serif;color:var(--ink)}

  .site-header{position:absolute;left:0;top:0;width:1200px;height:86px;
    background:linear-gradient(#ffffff,#f1f2f3);border-bottom:1px solid #d6d8da}
  .brand{position:absolute;left:258px;top:20px;display:flex;align-items:center;gap:8px}
  .brand-mark{width:44px;height:44px;border-radius:50%;border:4px solid var(--brand-blue)}
  .brand-name{font-family:"Montserrat",sans-serif;font-weight:700;font-size:17px;line-height:18px;
    color:#3d4148;letter-spacing:.5px}
  .utility-nav{position:absolute;top:10px;right:259px;display:flex;align-items:center;gap:14px;
    font-size:7.5px;color:#444}
  .join-btn{background:var(--brand-green);color:var(--white);font-weight:700;font-size:7.5px;
    width:50px;height:19px;display:flex;align-items:center;justify-content:center}
  .main-nav{position:absolute;top:46px;left:558px;display:flex;height:40px;
    font-family:"Montserrat",sans-serif;font-size:9.5px;color:#3b3b3b;letter-spacing:.2px}
  .main-nav a{display:block;padding:0 17px;height:40px;line-height:13px;padding-top:1px}
  .main-nav .is-active{color:var(--brand-blue);border-bottom:4px solid var(--brand-blue)}
  .main-nav a:last-child{padding-right:0}

  .hero{position:absolute;left:0;top:86px;width:1200px;height:472px;overflow:hidden}
  .hero-photo{position:absolute;inset:0;
    background:
      radial-gradient(ellipse 360px 300px at 1030px 180px,rgba(130,90,130,.75),transparent 70%),
      linear-gradient(180deg,#5f7ea4 0%,#8ea7c3 30%,#a9bdd2 55%,#6c86a6 80%,#2e3e58 100%)}
  .hero-title{position:absolute;left:259px;top:95px;font-family:"Montserrat",sans-serif;font-weight:400;
    font-size:35px;line-height:42px;color:var(--white);text-shadow:0 2px 6px rgba(0,0,0,.25)}

  .intro-panel{position:absolute;left:258px;top:258px;width:683px;height:173px;background:var(--panel)}
  .intro-copy{position:absolute;left:22px;top:29px;width:290px;font-size:11px;line-height:15.4px;color:#333}
  .intro-copy strong{font-weight:600;color:#222}
  .testimonial-heading{position:absolute;left:370px;top:27px;font-size:11px;font-weight:700;color:#444}
  .testimonial{position:absolute;left:339px;top:47px;width:318px;height:96px;background:var(--quote-blue);
    color:var(--white);padding:18px 30px 0 31px}
  .quote-tab{position:absolute;top:-5px;width:26px;height:30px}
  .quote-tab.left{left:-4px}.quote-tab.right{right:-5px}
  .testimonial p{font-size:8px;line-height:12px;font-weight:600}
  .testimonial .author{margin-top:14px;font-family:"Noto Serif",serif;font-size:8px;font-weight:400}
  .testimonial .org{font-size:5.8px;font-weight:400;letter-spacing:.1px}

  .glance-bar{position:absolute;left:258px;top:431px;width:683px;height:41px;background:var(--bar);
    display:flex;align-items:center;padding-left:22px;font-size:12px;color:var(--white)}
  .glance-label{font-family:"Montserrat",sans-serif;font-weight:700;color:var(--accent-green);margin-right:18px;font-size:11.5px}
  .glance-controls{position:absolute;right:21px;top:13px;display:flex;gap:2px}
  .glance-controls span{width:16px;height:16px;display:flex;align-items:center;justify-content:center}
  .ctrl-prev{background:var(--brand-blue)}.ctrl-next{background:var(--white)}

  .site-footer{position:absolute;left:0;top:558px;width:1200px;height:43px;background:var(--footer);
    color:#e6e6e6;font-size:7.5px;letter-spacing:.2px}
  .copyright{position:absolute;left:280px;top:17px}
  .footer-links{position:absolute;right:280px;top:17px;display:flex;gap:24px}
</style>
</head>
<body>
  <header class="site-header">
    <div class="brand"><span class="brand-mark"></span><span class="brand-name">VERLOW<br>PARTNERS</span></div>
    <nav class="utility-nav"><span>Contact Us</span><span>FAQS</span><span class="join-btn">JOIN US</span></nav>
    <nav class="main-nav">
      <a class="is-active">HOME</a><a>ABOUT VERLOW</a><a>OUR VALUES</a><a>CLIENTS &amp; SERVICES</a>
    </nav>
  </header>

  <section class="hero">
    <div class="hero-photo" role="img" aria-label="Dusk city skyline with a curving purple steel bridge structure"></div>
    <h1 class="hero-title">Where Strategy,<br>Operations, and People<br>Deliver Performance</h1>

    <div class="intro-panel">
      <p class="intro-copy"><strong>Verlow Partners</strong> manages a network of over 300 experienced, independent professionals from diverse industry and functional backgrounds. Our mission is to provide best-of-class, customized advisory services for clients. We address issues relating to top-line growth, cost-optimisation, and other performance issues to build shareholder value.</p>
      <h2 class="testimonial-heading">What clients have to say....</h2>
      <blockquote class="testimonial">
        <svg class="quote-tab left" viewBox="0 0 26 30"><path d="M0 0H26V30L13 23L0 30Z" fill="#3aa845"/><text x="13" y="20" text-anchor="middle" font-size="18" font-weight="700" fill="#1f7a2c" font-family="Georgia,serif">“</text></svg>
        <svg class="quote-tab right" viewBox="0 0 26 30"><path d="M0 0H26V30L13 23L0 30Z" fill="#3aa845"/><text x="13" y="20" text-anchor="middle" font-size="18" font-weight="700" fill="#1f7a2c" font-family="Georgia,serif">”</text></svg>
        <p>Verlow accomplished an incredible amount during time we worked together, and, to this day, their contribution to the company are still apparent.</p>
        <p class="author">Chief Operating Officer</p>
        <p class="org">TECHNOLOGY COMPANY SERVICE THE DEFENCE SECTOR</p>
      </blockquote>
    </div>

    <div class="glance-bar">
      <span class="glance-label">VERLOW AT A GLANCE:</span>
      <span>We partner with our clients to deliver results.</span>
      <div class="glance-controls">
        <span class="ctrl-prev"><svg width="8" height="8" viewBox="0 0 8 8"><path d="M5.5 1L2.5 4L5.5 7" stroke="#fff" stroke-width="1.6" fill="none"/></svg></span>
        <span class="ctrl-next"><svg width="8" height="8" viewBox="0 0 8 8"><path d="M2.5 1L5.5 4L2.5 7" stroke="#111" stroke-width="1.6" fill="none"/></svg></span>
      </div>
    </div>
  </section>

  <footer class="site-footer">
    <span class="copyright">COPYRIGHT © 2014 VERLOW–PARTNERS LLC. ALL RIGHTS RESERVED.</span>
    <nav class="footer-links"><span>SITEMAP</span><span>TERMS OF USE</span><span>PRIVACY POLICY</span></nav>
  </footer>
</body>
</html>
```